Cover-Design für Office Notizbuch gesucht
Zielgruppe
Wir erstellen schöne Officeprodukte für junge, modebewusste (und alte) Mädels. Es soll also sehr quillorat / moranteve tauglich sein.
Aufgabenstellung
Wir möchten ein Din A5 Notizbuch haben und suchen dafür ein tolles Coverdesign.
Es soll ein zeitloses Design haben, gerne mit einem motivierenden Spruch oder einfach einem schönen Muster und Design.
Zusätzlich kann auch mit einer Heißfolienprägung Gold gearbeitet werden.

```html
<!DOCTYPE html>
<html lang="de">
<head>
<meta charset="utf-8">
<title>Notizbuch Cover – Gedanken</title>
<link rel="stylesheet" href="https://fonts.googleapis.com/css2?family=Playball&family=Great+Vibes&display=swap">
<style>
  :root {
    --backdrop: #fbe9e0;
    --paper: #fbfafa;
    --paper-edge: #e9e4e3;
    --ink: #8a7f7c;
    --petal: #f3b8bd;
    --petal-deep: #e88e98;
    --petal-pale: #fbe1e2;
  }
  html, body {
    margin: 0;
    padding: 0;
    width: 1200px;
    height: 1105px;
    overflow: hidden;
    background: var(--backdrop);
  }
  .canvas {
    position: relative;
    width: 1200px;
    height: 1105px;
    background: var(--backdrop);
  }
  .cover {
    position: absolute;
    left: 253px;
    top: 62px;
    width: 693px;
    height: 980px;
    background: var(--paper);
    box-shadow: inset 6px 0 0 var(--paper-edge);
    overflow: hidden;
  }
  .floral {
    position: absolute;
  }
  .floral--top {
    left: 180px;
    top: 0;
    width: 513px;
    height: 380px;
    background:
      radial-gradient(ellipse 90px 80px at 420px 70px, var(--petal-deep) 0%, var(--petal) 45%, transparent 100%),
      radial-gradient(ellipse 130px 110px at 240px 250px, var(--petal-pale) 0%, var(--petal) 60%, transparent 100%),
      radial-gradient(ellipse 90px 70px at 130px 90px, var(--petal) 0%, var(--petal-pale) 60%, transparent 100%);
  }
  .floral--left {
    left: 0;
    top: 270px;
    width: 320px;
    height: 320px;
    background: radial-gradient(ellipse 150px 140px at 120px 150px, var(--petal-deep) 0%, var(--petal) 40%, var(--petal-pale) 75%, transparent 100%);
  }
  .floral--bottom {
    left: 520px;
    top: 470px;
    width: 173px;
    height: 260px;
    background: radial-gradient(ellipse 110px 120px at 130px 120px, var(--petal) 0%, var(--petal-pale) 65%, transparent 100%);
  }
  .quote {
    position: absolute;
    left: 90px;
    top: 585px;
    width: 540px;
    margin: 0;
    color: var(--ink);
    font-weight: 400;
  }
  .quote__line {
    display: block;
    font-family: "Playball", cursive;
    font-size: 46px;
    line-height: 1.05;
  }
  .quote__line--indent {
    padding-left: 110px;
  }
  .quote__key {
    display: block;
    font-family: "Great Vibes", cursive;
    font-size: 130px;
    line-height: 1;
    padding-left: 60px;
  }
  .quote__line--end {
    text-align: right;
    padding-right: 10px;
    margin-top: -12px;
  }
</style>
</head>
<body>
<main class="canvas">
  <section class="cover" aria-label="Notizbuch Cover">
    <div class="floral floral--top" role="img" aria-label="Aquarell-Blüten in Rosa, obere rechte Ecke"></div>
    <div class="floral floral--left" role="img" aria-label="Große rosa Aquarell-Blüte, links"></div>
    <div class="floral floral--bottom" role="img" aria-label="Rosa Aquarell-Blüte am rechten Rand"></div>
    <p class="quote">
      <span class="quote__line">Ich wäre jetzt lieber</span>
      <span class="quote__line quote__line--indent">dort wo meine</span>
      <span class="quote__key">Gedanken</span>
      <span class="quote__line quote__line--end">gerade sind.</span>
    </p>
  </section>
</main>
</body>
</html>
```